Inflatable Movie Screen company needs a Brochure Design for sales kit

We need a brochure as per attached sketch drawing which is to:
1)follow the sample layout
2) attached images must be used
3) to follow company corporate colors or suggest something professional and appropriate for the theme
Updates

Target Market(s)

Corporate and Community Clubs

Industry/Entity Type

Entertainment

Requirements
Must have
• Colors to be in line with corporate colors OR to suggest something appropriate.
Nice to have
• A unique concept
Should not have
• Too fanciful

```html
<!DOCTYPE html>
<html lang="en">
<head>
<meta charset="utf-8">
<title>Lumaro Inflatable Movie Screening Brochure</title>
<link rel="stylesheet" href="https://fonts.googleapis.com/css2?family=Oswald:wght@400;600;700&family=Open+Sans:wght@400;600;700&display=swap">
<style>
:root{
  --stage:#5f6c64;
  --ink:#1b1b1d;
  --charcoal:#2a2b2f;
  --steel:#8d9096;
  --silver:#d9dbdf;
  --paper:#f3f3f4;
  --gold:#c9a35a;
  --orange:#e8892b;
  --plum:#6b2a5c;
  --berry:#8f1f4e;
  --text:#444549;
  --white:#ffffff;
}
*{box-sizing:border-box;margin:0;padding:0}
html,body{width:835px;height:1200px;overflow:hidden}
body{background:var(--stage);font-family:"Open Sans",Arial,sans-serif;color:var(--text);position:relative}
.spread{position:absolute;left:20px;width:795px;height:560px;display:flex;box-shadow:0 6px 18px rgba(0,0,0,.35);overflow:hidden}
.spread--outside{top:30px}
.spread--inside{top:620px}
.page{position:relative;width:50%;height:100%;overflow:hidden}
.photo{position:absolute;background:linear-gradient(135deg,#39414d,#7c8a96);}

/* ---------- outside: back cover ---------- */
.back-cover{background:linear-gradient(180deg,var(--white),var(--paper) 60%,#dcdde0)}
.back-cover__intro{position:absolute;left:34px;top:40px;width:250px;font-size:8px;line-height:1.55}
.back-cover__name{position:absolute;left:34px;top:120px;font-family:"Oswald",sans-serif;font-weight:700;font-size:15px;letter-spacing:1px;color:var(--ink)}
.contact{position:absolute;left:34px;top:150px;width:200px;border:1px solid #c6c8cc;background:var(--white)}
.contact__title{background:var(--steel);color:var(--white);font-family:"Oswald",sans-serif;font-size:10px;letter-spacing:1px;padding:4px 8px}
.contact__list{list-style:none;padding:6px 8px;font-size:8px;line-height:1.3}
.contact__list li{display:flex;align-items:center;gap:6px;margin:4px 0}
.contact__list svg{width:9px;height:9px;flex:none;fill:var(--steel)}
.back-cover__photo{left:34px;top:330px;width:250px;height:170px;border-radius:110px 16px 16px 16px;background:linear-gradient(160deg,#1d2333,#4a3f6b 55%,#2b6b8f)}

/* ---------- outside: front cover ---------- */
.front-cover{background:linear-gradient(170deg,#0d0d0f,#2c2d31 55%,#b9bbbf 78%,#e5e6e8)}
.front-cover__title{position:absolute;right:30px;top:26px;text-align:right;color:var(--white);font-family:"Oswald",sans-serif;text-transform:uppercase;line-height:1}
.front-cover__title span{display:block;font-size:20px;letter-spacing:2px;font-weight:400}
.front-cover__title strong{display:block;font-size:42px;font-weight:700;letter-spacing:1px}
.front-cover__photo{left:40px;top:90px;width:230px;height:150px;border-radius:50%;border:4px solid var(--silver);background:linear-gradient(180deg,#274b7a,#5a86b4 50%,#2f4f2a)}
.front-cover__caption{position:absolute;right:30px;top:265px;width:140px;text-align:right;font-size:7.5px;line-height:1.5;color:var(--silver)}
.brand-band{position:absolute;right:0;bottom:40px;width:210px;height:46px;background:linear-gradient(90deg,#6f7278,#9a9da3);display:flex;align-items:center;justify-content:center;gap:8px}
.brand-band__name{font-family:"Oswald",sans-serif;font-weight:600;font-size:22px;letter-spacing:3px;color:var(--white)}
.brand-band__dot{width:10px;height:10px;border-radius:50%;background:var(--white)}

/* ---------- inside: left ---------- */
.inside-left{background:linear-gradient(180deg,#e9eaec,#f7f7f8)}
.section-bar{position:absolute;left:0;height:20px;padding:0 14px 0 26px;background:var(--charcoal);color:var(--white);font-family:"Oswald",sans-serif;font-size:10px;letter-spacing:1px;display:flex;align-items:center;border-radius:0 10px 10px 0}
.reason{position:absolute;left:26px;width:250px;display:flex;gap:10px}
.reason__num{font-family:"Oswald",sans-serif;font-weight:700;font-size:30px;line-height:1;color:var(--charcoal)}
.reason__text{font-size:7.5px;line-height:1.5}
.reason__text b{display:block;font-size:8.5px;color:var(--ink)}
.reason__photo{right:26px;width:70px;height:70px;border-radius:50%;border:3px solid var(--white)}
.event-question{position:absolute;left:26px;top:292px;font-family:"Oswald",sans-serif;font-size:13px;color:var(--orange);letter-spacing:.5px}
.expect{position:absolute;left:26px;top:318px;width:345px;list-style:none;display:grid;grid-template-columns:1fr 1fr;gap:8px 14px;font-size:8px}
.expect li{display:flex;align-items:center;gap:6px}
.expect svg{width:14px;height:14px;flex:none}
.arch{bottom:22px;width:108px;height:110px;border-radius:54px 54px 6px 6px;border:3px solid var(--white)}

/* ---------- inside: right ---------- */
.inside-right{background:linear-gradient(180deg,#f4f4f5,#e4e5e8)}
.gallery{position:absolute;left:26px;top:52px;width:345px;display:grid;grid-template-columns:repeat(4,1fr);gap:5px}
.gallery .photo{position:relative;height:62px}
.inside-right__note{position:absolute;left:26px;top:198px;width:345px;font-size:8px;line-height:1.5;text-align:center}
.badges{position:absolute;left:40px;top:250px;width:315px;display:flex;justify-content:space-around}
.badge{width:62px;height:62px;border-radius:50%;background:var(--silver);border:3px solid var(--white)}
.badge--shield{border-radius:10px 10px 31px 31px;background:#c7c9cd}
.book-now{position:absolute;left:40px;top:362px;width:120px;height:54px;border-radius:27px;background:linear-gradient(180deg,var(--berry),var(--plum));color:var(--white);font-family:"Oswald",sans-serif;font-weight:700;font-size:20px;letter-spacing:1px;display:flex;align-items:center;justify-content:center;border:3px solid var(--white);box-shadow:0 2px 6px rgba(0,0,0,.3)}
.offer{position:absolute;left:0;bottom:0;width:100%;height:110px;background:linear-gradient(100deg,#3b1636,var(--plum) 60%,var(--berry))}
.offer__text{position:absolute;right:28px;top:22px;width:190px;text-align:right;color:var(--white);font-size:8px;line-height:1.45}
.offer__deal{display:block;font-family:"Oswald",sans-serif;font-weight:700;font-size:34px;line-height:1.1;color:var(--gold)}
.spine-shade{position:absolute;top:0;left:50%;width:20px;height:100%;margin-left:-10px;background:linear-gradient(90deg,transparent,rgba(0,0,0,.12),transparent);pointer-events:none}
.swoosh{position:absolute;inset:0;width:100%;height:100%;pointer-events:none}
</style>
</head>
<body>

<!-- Outside spread -->
<section class="spread spread--outside" aria-label="Brochure outside">
  <div class="page back-cover">
    <p class="back-cover__intro">We bring the big screen outdoors with fully managed inflatable cinema nights for clubs, schools, councils and corporate teams across the region.</p>
    <p class="back-cover__name">DALE MORAN</p>
    <div class="contact">
      <div class="contact__title">CONTACT US</div>
      <ul class="contact__list">
        <li><svg viewBox="0 0 10 10"><path d="M5 0a3.5 3.5 0 0 0-3.5 3.5C1.5 6 5 10 5 10s3.5-4 3.5-6.5A3.5 3.5 0 0 0 5 0zm0 5a1.5 1.5 0 1 1 0-3 1.5 1.5 0 0 1 0 3z"/></svg>18 Harbour Lane, Eastfield VIC 3041</li>
        <li><svg viewBox="0 0 10 10"><path d="M2 0l2 2.5-1.2 1.3a6 6 0 0 0 3.4 3.4L7.5 6 10 8l-1.5 2C4 10 0 6 0 1.5z"/></svg>+61 3 5550 0148</li>
        <li><svg viewBox="0 0 10 10"><path d="M0 2h10v6H0zM0 2l5 3.5L10 2" stroke="#fff" stroke-width=".8"/></svg>hello@lumaroscreens.com</li>
        <li><svg viewBox="0 0 10 10"><circle cx="5" cy="5" r="4.5"/></svg>www.lumaroscreens.com</li>
      </ul>
    </div>
    <div class="photo back-cover__photo" role="img" aria-label="Audience watching a film in a darkened indoor cinema setup"></div>
  </div>
  <div class="page front-cover">
    <h1 class="front-cover__title"><span>Inflatable</span><strong>Movie</strong><span>Screening</span></h1>
    <div class="photo front-cover__photo" role="img" aria-label="Giant inflatable movie screen set up on a lawn at dusk"></div>
    <p class="front-cover__caption">Outdoor cinema made simple, from setup to final credits.</p>
    <div class="brand-band"><span class="brand-band__dot"></span><span class="brand-band__name">LUMARO</span></div>
  </div>
  <svg class="swoosh" viewBox="0 0 795 560" preserveAspectRatio="none" aria-hidden="true">
    <path d="M330 560 C360 380 390 200 520 0 L545 0 C420 200 385 380 360 560 Z" fill="#c9cbd0"/>
    <path d="M355 560 C382 380 420 200 548 0 L556 0 C430 200 394 380 366 560 Z" fill="#c9a35a"/>
    <path d="M366 560 C394 380 430 200 556 0 L600 0 C470 210 430 390 410 560 Z" fill="#e6e7ea" opacity=".85"/>
  </svg>
  <div class="spine-shade"></div>
</section>

<!-- Inside spread -->
<section class="spread spread--inside" aria-label="Brochure inside">
  <div class="page inside-left">
    <div class="section-bar" style="top:22px">WHY CHOOSE US</div>
    <div class="reason" style="top:56px"><span class="reason__num">1</span><p class="reason__text"><b>Complete setup</b>Screen, projector and sound delivered, installed and run by our crew.</p></div>
    <div class="photo reason__photo" style="top:50px" role="img" aria-label="Crew inflating a large outdoor screen"></div>
    <div class="reason" style="top:126px"><span class="reason__num">2</span><p class="reason__text"><b>Any venue</b>Parks, sports ovals, school grounds and rooftops of many sizes.</p></div>
    <div class="photo reason__photo" style="top:120px" role="img" aria-label="Outdoor screening on a sports oval"></div>
    <div class="reason" style="top:196px"><span class="reason__num">3</span><p class="reason__text"><b>Fair pricing</b>Clear packages for clubs and companies with no hidden extras.</p></div>
    <div class="photo reason__photo" style="top:190px" role="img" aria-label="Families seated on the grass before a film"></div>
    <div class="section-bar" style="top:266px">WHAT TO EXPECT</div>
    <p class="event-question">CELEBRATING AN EVENT?</p>
    <ul class="expect">
      <li><svg viewBox="0 0 14 14"><circle cx="7" cy="7" r="7" fill="#e8892b"/><path d="M4 7l2 2 4-4" stroke="#fff" stroke-width="1.5" fill="none"/></svg>Corporate movie nights</li>
      <li><svg viewBox="0 0 14 14"><circle cx="7" cy="7" r="7" fill="#e8892b"/><path d="M4 7l2 2 4-4" stroke="#fff" stroke-width="1.5" fill="none"/></svg>Community club events</li>
      <li><svg viewBox="0 0 14 14"><circle cx="7" cy="7" r="7" fill="#e8892b"/><path d="M4 7l2 2 4-4" stroke="#fff" stroke-width="1.5" fill="none"/></svg>School fundraisers</li>
      <li><svg viewBox="0 0 14 14"><circle cx="7" cy="7" r="7" fill="#e8892b"/><path d="M4 7l2 2 4-4" stroke="#fff" stroke-width="1.5" fill="none"/></svg>Sports broadcasts</li>
      <li><svg viewBox="0 0 14 14"><circle cx="7" cy="7" r="7" fill="#e8892b"/><path d="M4 7l2 2 4-4" stroke="#fff" stroke-width="1.5" fill="none"/></svg>Birthday parties</li>
      <li><svg viewBox="0 0 14 14"><circle cx="7" cy="7" r="7" fill="#e8892b"/><path d="M4 7l2 2 4-4" stroke="#fff" stroke-width="1.5" fill="none"/></svg>Product launches</li>
    </ul>
    <div class="photo arch" style="left:20px" role="img" aria-label="Inflatable screen at an evening park event"></div>
    <div class="photo arch" style="left:144px" role="img" aria-label="Crowd on picnic rugs facing the screen"></div>
    <div class="photo arch" style="left:268px" role="img" aria-label="Screen glowing beside trees at night"></div>
  </div>
  <div class="page inside-right">
    <div class="section-bar" style="top:22px">OUR EVENTS</div>
    <div class="gallery">
      <div class="photo" role="img" aria-label="Outdoor screening at a sports club"></div>
      <div class="photo" role="img" aria-label="Screen on a beach at sunset"></div>
      <div class="photo" role="img" aria-label="Corporate guests at an evening screening"></div>
      <div class="photo" role="img" aria-label="Night screening in a town square"></div>
      <div class="photo" role="img" aria-label="Families on a lawn before the film"></div>
      <div class="photo" role="img" aria-label="Screen at a school oval"></div>
      <div class="photo" role="img" aria-label="Audience seated under string lights"></div>
      <div class="photo" role="img" aria-label="Screen set up in a courtyard"></div>
    </div>
    <p class="inside-right__note">Let us organise a movie experience your guests will remember. Trusted by clubs and companies across the state.</p>
    <div class="badges">
      <div class="badge" role="img" aria-label="Partner badge"></div>
      <div class="badge badge--shield" role="img" aria-label="Club badge"></div>
      <div class="badge" role="img" aria-label="Community partner badge"></div>
    </div>
    <div class="book-now">BOOK NOW</div>
    <div class="offer">
      <p class="offer__text">Book your first screening with us this season and save on any package<span class="offer__deal">20% OFF</span></p>
    </div>
  </div>
  <div class="spine-shade"></div>
</section>

</body>
</html>
```